Design a new product for a successful cannabis company

We need a package design for a new brand. We are a large cannabis company near Seattle, USA. The name of the product is called the "Velmora Quill". It is a pure cannabis oil extract that is used through a magnetic vaporizer cartridge. We need a graphic template designed that will be printed on a card and inserted into the plastic packaging. This project is design the overall concept, and we will add the required warnings on our end once a design is chosen.

Dimensions:
Width - 2.5625 inches
Height - 3.3125 inches
Viewing Window Width - .4375 inches
Viewing Window Height - 2.0 Inches
Distance from the bottom of the card to the viewing window- .4375 inches
Distance from the left side to the viewing window - 1.0625 inch
Distance from the right side to the viewing window - 1.0625 inch

Theme:
- We would like it to have some sort of Velmora Quill historical feel. I attached the dimensions for size reference. Please extract that "VelmoraQuill" text/font if possible. We really want to use that.
- You could use an old map from that region and time in history.
- Wiki link explaining the Velmora Quill (https://en.lorevault.example/wiki/Velmora_Quill)

Additional Notes:
- There is an area where the physical cartridge will go. Feel free to extend the background into that area but please do not place any text there.
- There is a backside of this package that customers will see. We will place our warning text back there along with a product description. Please keep the back side clear of text but have it match whatever color scheme or background you do on the front side.
- I included an example of a competitor using the same package shape. That's what it will be printed on

Please reach out if you have questions or need clarification. I will be adding details as we go to help with the concept. Thank you!

Target Market(s)

Cannabis oil users of all ages

Colors

Designer to choose colors to be used in the design.

Requirements
Must have
• The same VelmoraQuill text from the attached concert poster
• Must say "A magnetic vape cartridge."
Nice to have
• A historical feel by faintly using an 12th century English map as the background. Open to anything in order to achieve a classic feel.
Should not have
• Bright colors

```html
<!DOCTYPE html>
<html lang="en">
<head>
<meta charset="utf-8">
<title>Velmora Quill – Magnetic Vape Cartridge Card</title>
<link rel="stylesheet" href="https://fonts.googleapis.com/css2?family=Federant&family=Almendra:wght@700&display=swap">
<style>
  :root {
    --page-bg: #e2c89c;
    --parchment-light: #ecd39a;
    --parchment-mid: #d9b36a;
    --parchment-deep: #b98a3c;
    --ink: #1b150e;
    --window-fill: #f7f7f5;
    --window-edge: #2a2a2a;
    --brass-light: #f1dcb8;
    --brass-deep: #b8863a;
    --wood: #7a4a22;
  }
  html, body {
    margin: 0;
    width: 1200px;
    height: 1200px;
    overflow: hidden;
    background: var(--page-bg);
  }
  .stage {
    position: relative;
    width: 1200px;
    height: 1200px;
  }
  .card {
    position: absolute;
    left: 182px;
    top: 60px;
    width: 836px;
    height: 1080px;
    border-radius: 22px;
    overflow: hidden;
    box-shadow: 0 6px 18px rgba(90, 60, 20, 0.25);
  }
  .card__map {
    position: absolute;
    inset: 0;
    background:
      radial-gradient(ellipse at 35% 30%, var(--parchment-light) 0%, transparent 60%),
      radial-gradient(ellipse at 80% 70%, rgba(185, 138, 60, 0.55) 0%, transparent 55%),
      linear-gradient(160deg, var(--parchment-mid) 0%, var(--parchment-light) 45%, var(--parchment-deep) 100%);
  }
  .card__hang-slot {
    position: absolute;
    left: 318px;
    top: 78px;
    width: 200px;
    height: 50px;
    border-radius: 25px;
    background: var(--page-bg);
    box-shadow: inset 0 3px 6px rgba(90, 60, 20, 0.35);
  }
  .card__title {
    position: absolute;
    left: 0;
    right: 0;
    top: 150px;
    margin: 0;
    text-align: center;
    font-family: "Federant", serif;
    font-weight: 400;
    font-size: 104px;
    line-height: 1;
    letter-spacing: 1px;
    text-transform: uppercase;
    color: var(--ink);
    transform: scaleY(1.2);
  }
  .card__window {
    position: absolute;
    left: 84px;
    top: 370px;
    width: 118px;
    height: 640px;
    background: var(--window-fill);
    border: 5px solid var(--window-edge);
    box-sizing: border-box;
  }
  .card__tagline {
    position: absolute;
    left: 250px;
    width: 560px;
    top: 400px;
    margin: 0;
    text-align: center;
    font-family: "Almendra", serif;
    font-weight: 700;
    font-size: 68px;
    line-height: 1.02;
    color: var(--ink);
  }
  .card__compass {
    position: absolute;
    left: 250px;
    top: 640px;
    width: 560px;
    height: 560px;
    border-radius: 50%;
    background: radial-gradient(circle at 50% 55%, var(--brass-light) 0%, #e6c89a 55%, var(--brass-deep) 72%, var(--parchment-deep) 100%);
  }
  .card__base-band {
    position: absolute;
    left: 0;
    right: 0;
    bottom: 0;
    height: 18px;
    background: var(--wood);
    opacity: 0.55;
  }
</style>
</head>
<body>
  <main class="stage">
    <section class="card">
      <div class="card__map" role="img" aria-label="Faded antique parchment map in warm gold and brown tones"></div>
      <div class="card__hang-slot"></div>
      <h1 class="card__title">Velmora Quill</h1>
      <div class="card__compass" role="img" aria-label="Brass antique compass with a rose dial"></div>
      <div class="card__window"></div>
      <p class="card__tagline">A Magnetic<br>Vape<br>Cartridge</p>
      <div class="card__base-band"></div>
    </section>
  </main>
</body>
</html>
```